New Years Greeting Card Design Competition

We need a greeting card design for the new year 2014. We would like to have pictures of our daughter Meera on the card. Please find attached 5 photos of her. Please feel free to use all 5 or some of them for the design. We would like the following text on the card: "Happy New Year" and "Vik, Pooja, and Meera Deshpande." We would like to see designs that are very positive in style.

Target Market(s)

The greeting card is going to be sent to family and friends in different parts of the world.

Requirements
Must have
• We would like to have pictures of our daughter Meera on the card. Please find attached 5 photos of her. Please feel free to use all 5 or some of them for the design. We would like the following text on the card: "Happy New Year" and "Vik, Pooja, and Meera Deshpande."

```html
<!DOCTYPE html>
<html lang="en">
<head>
<meta charset="utf-8">
<title>Happy New Year 2014 – Deshpande Family</title>
<link rel="stylesheet" href="https://fonts.googleapis.com/css2?family=Great+Vibes&family=PT+Sans&display=swap">
<style>
  :root {
    --sand-light: #e2d6c1;
    --sand-mid: #d6c8ae;
    --sand-dark: #c9b899;
    --shell-cream: #efe3cf;
    --shell-tan: #c99a63;
    --shell-brown: #a56a35;
    --shell-wine: #7c2a2c;
    --ink-navy: #2a2977;
    --ink-dark: #2b2b2b;
    --photo-border: #ffffff;
    --photo-soft: #e9e4ec;
    --photo-lilac: #b7a7d8;
  }
  * { margin: 0; padding: 0; box-sizing: border-box; }
  html, body { width: 1200px; height: 878px; overflow: hidden; background: #f4f1ec; }
  .card {
    position: relative;
    width: 1200px;
    height: 878px;
    overflow: hidden;
    background:
      radial-gradient(ellipse at 30% 20%, var(--sand-light), transparent 60%),
      linear-gradient(160deg, var(--sand-light) 0%, var(--sand-mid) 55%, var(--sand-dark) 100%);
  }
  .shells {
    position: absolute;
    border-radius: 50%;
  }
  .shells--top-right {
    left: 745px; top: -40px; width: 520px; height: 620px;
    background: radial-gradient(ellipse at 60% 40%, var(--shell-cream) 0%, var(--shell-tan) 55%, rgba(201,154,99,0) 72%);
  }
  .shells--bottom-left {
    left: -90px; top: 650px; width: 520px; height: 300px;
    background: radial-gradient(ellipse at 40% 55%, var(--shell-cream) 0%, var(--shell-tan) 50%, rgba(201,154,99,0) 72%);
  }
  .shells--bottom-middle {
    left: 600px; top: 740px; width: 420px; height: 200px;
    background: radial-gradient(ellipse at 50% 55%, var(--shell-cream) 0%, var(--shell-tan) 50%, rgba(201,154,99,0) 72%);
  }
  .shells--bottom-right {
    left: 1080px; top: 560px; width: 200px; height: 360px;
    background: radial-gradient(ellipse at 55% 55%, var(--shell-wine) 0%, var(--shell-brown) 45%, rgba(165,106,53,0) 72%);
  }
  .greeting {
    position: absolute;
    left: 0; width: 1200px; top: 160px;
    text-align: center;
    font-family: "Great Vibes", cursive;
    font-weight: 400;
    font-size: 92px;
    line-height: 1;
    color: var(--ink-navy);
    padding-left: 5px;
  }
  .year-lettering {
    position: absolute;
    left: 445px; top: 268px; width: 322px; height: 120px;
    border-radius: 14px;
    background: linear-gradient(90deg, #d8604c 0%, #3e8bb8 30%, #e0a43a 55%, #7b4fa3 78%, #3aa17a 100%);
    opacity: 0.55;
  }
  .from {
    position: absolute;
    left: 0; width: 1200px; top: 404px;
    text-align: center;
    font-family: "Great Vibes", cursive;
    font-size: 28px;
    color: var(--ink-dark);
  }
  .family-names {
    position: absolute;
    left: 0; width: 1200px; top: 446px;
    text-align: center;
    font-family: "PT Sans", sans-serif;
    font-size: 25px;
    letter-spacing: 0.3px;
    color: var(--ink-dark);
  }
  .photo {
    position: absolute;
    border: 7px solid var(--photo-border);
    box-shadow: 0 3px 8px rgba(0,0,0,0.3);
    background: linear-gradient(150deg, var(--photo-soft) 0%, #d9c7c2 55%, var(--photo-lilac) 100%);
  }
  .photo--first  { left: 60px;  top: 548px; width: 300px; height: 230px; transform: rotate(-5deg); }
  .photo--second { left: 330px; top: 564px; width: 304px; height: 216px;
    background: linear-gradient(150deg, #3a3234 0%, #6b5f66 45%, #e6e3ea 100%); }
  .photo--third  { left: 573px; top: 518px; width: 295px; height: 215px; transform: rotate(-1deg); }
  .photo--fourth { left: 822px; top: 566px; width: 310px; height: 226px; transform: rotate(6deg);
    background: linear-gradient(150deg, #ece6e6 0%, #d8b8b4 55%, #e9b7c4 100%); }
</style>
</head>
<body>
<main class="card">
  <div class="shells shells--top-right" role="img" aria-label="Seashells scattered on the sand"></div>
  <div class="shells shells--bottom-left" role="img" aria-label="Spiky conch shell on the sand"></div>
  <div class="shells shells--bottom-middle" role="img" aria-label="Scallop shells on the sand"></div>
  <div class="shells shells--bottom-right" role="img" aria-label="Patterned red-brown shell"></div>

  <h1 class="greeting">Happy New Year</h1>
  <div class="year-lettering" role="img" aria-label="2014 lettered from small colourful numbers"></div>
  <p class="from">from</p>
  <p class="family-names">Vik, Pooja, and Meera Deshpande</p>

  <div class="photo photo--first" role="img" aria-label="Photo of baby Meera wrapped in a lilac blanket"></div>
  <div class="photo photo--second" role="img" aria-label="Photo of baby Meera in a car seat wearing a white cap"></div>
  <div class="photo photo--third" role="img" aria-label="Photo of baby Meera awake in a lilac blanket"></div>
  <div class="photo photo--fourth" role="img" aria-label="Photo of baby Meera in a pink fleece"></div>
</main>
</body>
</html>
```